New brand for digital company - your chance to get creative

We need to create a brand for our new business 'Lanternfish Digital'. Please read the brief below before progressing as we are looking for some quite specific outputs.

Background

We are positioning ourselves as ‘marketing technologists’ - we're helping businesses engage with their customers in the online space.

Our tactics include branding, marketing, online management, and social media, however we are differentiating ourselves by focusing on overall strategy, not just tactics. Our tagline is ‘Online made simple’.

We have stipulated some parameters for the brand but otherwise want designers to exercise their creativity.

Requirements
Must have
• We want to see an entire concept, not just a logo.

```html
<!DOCTYPE html>
<html lang="en">
<head>
<meta charset="utf-8">
<title>Lanternfish Digital — Online Made Easy</title>
<link rel="stylesheet" href="https://fonts.googleapis.com/css2?family=Fredoka:wght@600&display=swap">
<style>
  :root {
    --sun-yellow: #fbb91c;
    --photo-deep: #5f66aa;
    --photo-mid: #8d92cc;
    --photo-light: #b3b6e0;
    --flap-shade: #7a7fc4;
    --flap-light: #f4f4fb;
    --paper: #ffffff;
    --ink: #231f20;
  }
  * { margin: 0; padding: 0; box-sizing: border-box; }
  html, body { width: 1200px; height: 848px; overflow: hidden; background: var(--paper); }
  .poster { position: relative; width: 1200px; height: 848px; background: var(--paper); }

  .hero {
    position: absolute; left: 0; top: 0; width: 1200px; height: 716px;
    background:
      radial-gradient(ellipse 260px 420px at 680px 380px, rgba(40,45,110,0.55), transparent 70%),
      radial-gradient(ellipse 220px 460px at 420px 300px, rgba(235,235,250,0.45), transparent 70%),
      linear-gradient(100deg, var(--photo-deep) 0%, var(--photo-mid) 45%, var(--photo-light) 100%);
  }
  .corner-curl { position: absolute; left: 0; top: 0; }

  .corner-question {
    position: absolute; right: 32px; top: 28px;
    font-family: "Fredoka", sans-serif; font-weight: 600;
    font-size: 31px; line-height: 37px; text-transform: uppercase;
    text-align: right; color: var(--paper); letter-spacing: 0.5px;
  }
  .headline {
    position: absolute; left: 32px; top: 596px;
    font-family: "Fredoka", sans-serif; font-weight: 600;
    font-size: 84px; line-height: 90px; text-transform: uppercase;
    color: var(--paper); letter-spacing: 3px; white-space: nowrap;
  }
  .body-copy {
    position: absolute; left: 47px; top: 743px; width: 820px;
    font-family: Arial, Helvetica, sans-serif; font-size: 16px; line-height: 20.5px;
    color: var(--ink); white-space: nowrap;
  }
  .brand {
    position: absolute; right: 32px; top: 756px;
    display: flex; align-items: center; gap: 10px;
  }
  .brand-dot {
    width: 16px; height: 16px; border-radius: 50%;
    background: var(--sun-yellow);
  }
  .brand-name {
    font-family: "Fredoka", sans-serif; font-weight: 600;
    font-size: 26px; line-height: 32px;
    color: var(--ink); white-space: nowrap;
  }
</style>
</head>
<body>
<main class="poster">
  <div class="hero" role="img" aria-label="Motion-blurred photo of commuters walking past bicycles on a city pavement, tinted lavender blue"></div>

  <svg class="corner-curl" width="1200" height="716" viewBox="0 0 1200 716" aria-hidden="true">
    <defs>
      <linearGradient id="flapShade" x1="780" y1="60" x2="1010" y2="330" gradientUnits="userSpaceOnUse">
        <stop offset="0" stop-color="#7a7fc4"/>
        <stop offset="0.55" stop-color="#a9acdc"/>
        <stop offset="1" stop-color="#f4f4fb"/>
      </linearGradient>
    </defs>
    <polygon points="659,0 1200,0 1200,268" fill="#fbb91c"/>
    <path d="M659,0 C770,90 910,210 998,356 C1035,300 1100,272 1200,268 Z" fill="url(#flapShade)"/>
  </svg>

  <p class="corner-question">Looking for a<br>hassle-free online<br>marketing?</p>

  <h1 class="headline">Online made easy.</h1>

  <p class="body-copy">Lorem ipsum dolor sit amet, consectetuer adipiscing elit. Aenean commodo ligula eget dolor.<br>Aenean massa. Cum sociis natoque penatibus et magnis dis parturient montes, nascetur<br>ridiculus mus. Donec quam felis, ultricies nec, pellentesque eu, pretium quis, sem.</p>

  <div class="brand">
    <span class="brand-dot" aria-hidden="true"></span>
    <p class="brand-name">Lanternfish Digital</p>
  </div>
</main>
</body>
</html>
```